Velvet Glow Co. Derma Roller packaging design

I need a box designed for a skin care brand called Velvet Glow Co. The box will be for our Derma Roller- a skin rejuvenation device. It will be sold online with lots of competition. I would like a modern, high end design, something that stands out and looks amazing. My logo is blush pink and black, for packaging i need no more than 3 colours, maybe gold if any other colour is used. A photo of a sample derma roller is attached below for an idea of what the product looks like, however my roller with have a clear handle with a black roller. The roller comes in a clear case, the box dimensions will need to be 16 cm long, 4 cm high, 4.5 cm wide.
ATTACHED ARE 2 SAMPLE BOXES AS AN EXAMPLE OF THE SIZE OF BOX REQUIRED!

Target Market(s)

25-50 year old women in the US

Colors
e667a6
000000
efefef

Requirements
Must have
• LOGO
• NAME OF PRODUCT- Cosmetic Derma Roller
• NEEDLE DEPTH- 0.25mm
• CAUTION- For personal use only, Do not use if allergic to metal, Do not use on open skin, wounds or active acne, sterilise roller before and after use.
Nice to have
• BENEFITS- Skin Rejuvenation, Collagen Induction Therapy, Increase product absorption, reduce acne scars and pigmentation
• FEATURES- 540 high quality titanium needles, ultra sharp needle tips, cross-line needle arrangement, ergonomic handle, anti slip grip,

```html
<!DOCTYPE html>
<html lang="en">
<head>
<meta charset="utf-8">
<title>Velvet Glow Co. – Cosmetic Derma Roller packaging</title>
<link rel="stylesheet" href="https://fonts.googleapis.com/css2?family=Exo+2:ital,wght@1,800;1,900&family=Oswald:wght@300;400&display=swap">
<style>
  :root {
    --blush: #f7aed0;
    --blush-deep: #e667a6;
    --black: #000000;
    --ink: #141414;
    --charcoal: #3a393b;
    --paper: #ffffff;
    --stage: #e9e9e9;
    --steel: #8a8a8c;
    --silver: #c9c9cb;
    --light-text: #e4e4e4;
    --plum: #4a1a33;
  }
  * { box-sizing: border-box; margin: 0; padding: 0; }
  html, body { width: 1200px; height: 702px; overflow: hidden; }
  body {
    background: var(--stage); position: relative; font-family: "Oswald", sans-serif;
    -webkit-font-smoothing: antialiased; -moz-osx-font-smoothing: grayscale;
    text-rendering: geometricPrecision;
  }

  .panel {
    position: absolute; left: 233px; width: 734px; height: 205px; overflow: hidden;
  }
  .panel--dark { top: 119px; background: var(--charcoal); }
  .panel--light { top: 413px; background: var(--paper); }

  .panel__shapes { position: absolute; inset: 0; }

  .logo-tile {
    position: absolute; left: 27px; top: 22px; width: 161px; height: 160px;
    background: var(--blush);
  }
  .logo-tile__frame {
    position: absolute; left: 22px; top: 26px; width: 118px; height: 92px;
    border: 1px solid var(--ink);
  }
  .logo-tile__name {
    position: absolute; left: 0; right: 0; top: 66px; text-align: center;
    font-family: "Oswald", sans-serif; font-weight: 400; font-size: 17px;
    letter-spacing: 1px; color: var(--ink); white-space: nowrap;
  }

  .product-art {
    position: absolute; left: 200px; top: 33px; width: 380px; height: 60px;
    border-radius: 30px 18px 18px 30px;
  }
  .panel--dark .product-art { background: linear-gradient(90deg, rgba(255,255,255,.05), rgba(201,160,150,.18)); }
  .panel--light .product-art { background: linear-gradient(90deg, #f3f3f3, #dcdcdc); }

  .product-art__label {
    position: absolute; font-family: "Oswald", sans-serif; font-weight: 400;
    font-size: 8px; color: var(--steel); white-space: nowrap;
  }
  .product-art__label--grip { left: 374px; top: 52px; }
  .product-art__label--handle { left: 374px; top: 67px; }

  .needle-depth {
    position: absolute; left: 572px; top: 56px; transform: rotate(90deg);
    transform-origin: left top;
    font-family: "Oswald", sans-serif; font-weight: 400; font-size: 10px; white-space: nowrap;
  }
  .needle-depth { left: 598px; top: 38px; }
  .panel--dark .needle-depth { color: var(--paper); }
  .panel--light .needle-depth { color: var(--ink); }

  .product-title {
    position: absolute; left: 190px; top: 127px; width: 406px;
    font-family: "Exo 2", sans-serif; font-style: italic; font-weight: 900;
    font-size: 29px; line-height: 1; white-space: nowrap; letter-spacing: .3px;
  }
  .panel--dark .product-title__lead { color: var(--steel); }
  .panel--dark .product-title__name { color: var(--silver); }
  .panel--light .product-title__lead { color: var(--black); }
  .panel--light .product-title__name { color: #5c5c5e; }

  .title-rule {
    position: absolute; left: 191px; top: 159px; width: 405px; height: 2px;
    background: var(--blush);
  }

  .benefits {
    position: absolute; left: 193px; top: 164px; width: 405px;
    font-family: "Oswald", sans-serif; font-weight: 400; font-size: 9.5px;
    line-height: 12px; white-space: nowrap; letter-spacing: -.15px;
  }
  .panel--dark .benefits { color: var(--light-text); }
  .panel--light .benefits { color: var(--plum); }

  .features { position: absolute; right: 20px; top: 94px; list-style: none; }
  .features__item {
    position: relative; text-align: right; padding-right: 7px; margin-bottom: 10px;
    font-family: "Oswald", sans-serif; font-weight: 400; font-size: 9px;
    line-height: 11px; color: var(--paper);
  }
  .features__item::after {
    content: ""; position: absolute; right: 0; top: 2px; width: 2px; height: 18px;
    background: var(--blush-deep);
  }
</style>
</head>
<body>

<section class="panel panel--dark" aria-label="Front panel, dark version">
  <svg class="panel__shapes" width="734" height="205" viewBox="0 0 734 205">
    <defs>
      <pattern id="teeth-dark" width="10" height="4" patternUnits="userSpaceOnUse">
        <polygon points="10,0 0,2 10,4" fill="#000"/>
      </pattern>
    </defs>
    <polygon points="0,0 164,0 60,205 0,205" fill="#000"/>
    <polygon points="712,0 734,0 734,205 596,205" fill="#000"/>
    <g transform="translate(712,0) rotate(29.5)">
      <rect x="-10" y="0" width="10" height="236" fill="url(#teeth-dark)"/>
    </g>
  </svg>

  <div class="logo-tile">
    <div class="logo-tile__frame"></div>
    <div class="logo-tile__name">Velvet Glow Co.</div>
  </div>

  <div class="product-art" role="img" aria-label="Line drawing of the derma roller with handle and needle head"></div>
  <span class="product-art__label product-art__label--grip">anti slip grip</span>
  <span class="product-art__label product-art__label--handle">ergonomic handle</span>
  <span class="needle-depth">0.25mm</span>

  <h1 class="product-title"><span class="product-title__lead">COSMETIC</span> <span class="product-title__name">DERMA ROLLER</span></h1>
  <div class="title-rule"></div>
  <p class="benefits">Skin Rejuvenation, Collagen Induction Therapy, Increase product absorption, reduce acne scars and pigmentation</p>

  <ul class="features">
    <li class="features__item">Ultra sharp<br>needle tips</li>
    <li class="features__item">540 high quality<br>Titanium needles</li>
    <li class="features__item">Cross-line needle<br>arrangement</li>
  </ul>
</section>

<section class="panel panel--light" aria-label="Front panel, light version">
  <svg class="panel__shapes" width="734" height="205" viewBox="0 0 734 205">
    <defs>
      <pattern id="teeth-light" width="10" height="4" patternUnits="userSpaceOnUse">
        <polygon points="10,0 0,2 10,4" fill="#000"/>
      </pattern>
    </defs>
    <polygon points="0,0 164,0 60,205 0,205" fill="#000"/>
    <polygon points="712,0 734,0 734,205 596,205" fill="#000"/>
    <g transform="translate(712,0) rotate(29.5)">
      <rect x="-10" y="0" width="10" height="236" fill="url(#teeth-light)"/>
    </g>
  </svg>

  <div class="logo-tile">
    <div class="logo-tile__frame"></div>
    <div class="logo-tile__name">Velvet Glow Co.</div>
  </div>

  <div class="product-art" role="img" aria-label="Line drawing of the derma roller with handle and needle head"></div>
  <span class="product-art__label product-art__label--grip">anti slip grip</span>
  <span class="product-art__label product-art__label--handle">ergonomic handle</span>
  <span class="needle-depth">0.25mm</span>

  <h2 class="product-title"><span class="product-title__lead">COSMETIC</span> <span class="product-title__name">DERMA ROLLER</span></h2>
  <div class="title-rule"></div>
  <p class="benefits">Skin Rejuvenation, Collagen Induction Therapy, Increase product absorption, reduce acne scars and pigmentation</p>

  <ul class="features">
    <li class="features__item">Ultra sharp<br>needle tips</li>
    <li class="features__item">540 high quality<br>Titanium needles</li>
    <li class="features__item">Cross-line needle<br>arrangement</li>
  </ul>
</section>

</body>
</html>
```